Joomla Responsive Website Template for an International Biotechnology Company

Our client is a biotechnology company that uses silver-based technology to help make products antimicrobial, antibacterial, and anti fungal. We need a Joomla-based template that is responsive/mobile friendly when viewed on tablets or smartphones. We are looking for a template design for the home page and subpages. We are replacing the current website http://www.velmora-labs.com with a new website being built here: http://velmoraclean.com.stagehost.com/velmoraprime/. What we have now on the site is the basic wire frame. This is the desired layout and pictures we want to use. We would like you to add some design elements to make the website more professional looking and polished. Please refer to the attached style guide to help you in choosing the color. The client does like the green leaf, which is included in the last page of style guide and may be good for a background image. While the Velmora logo and leaf are green, we do not want to overuse the color green. The client does own other technologies that we will be promoting on the site and the logos for these technologies are attached below. These logos are Tusk, Velmora-Prime, and Wisp. We will be using this website to promote the technologies, the markets the technologies serve; drinking water, medical devices, apparel and textiles, and architectural surfaces, and to promote the customer using these devices. Please make the design "clean" and not cluttered, as these technologies are used to fight "dirty things".
Updates

Hello Designers! Thank you all very much for your design submissions. They were simply excellent. Due to the Holidays and New Years, many of the client's team members have been on vacation. We expect to have feedback shortly and pick the top design soon there after. Again, thank you all very much and hope the New Year brings you continued success. Best, Dorian

Industry/Entity Type

Biotechnology

Coding

Coded - Design and coding required

```html
<!DOCTYPE html>
<html lang="en">
<head>
<meta charset="utf-8">
<title>Velmora Antimicrobial</title>
<link href="https://fonts.googleapis.com/css2?family=Open+Sans:wght@400;600;700;800&display=swap" rel="stylesheet">
<style>
:root{
  --green:#6cbd45;
  --green-dark:#4e9a2c;
  --ink:#444;
  --muted:#888;
  --band:#efefef;
  --line:#dcdcdc;
  --white:#fff;
  --dark:#2b2b2b;
}
*{box-sizing:border-box;margin:0;padding:0}
html,body{width:1200px;height:2604px;overflow:hidden}
body{font-family:"Open Sans",Arial,sans-serif;color:var(--ink);background:var(--white);position:relative}
.abs{position:absolute}
/* header */
.brand{left:120px;top:30px;display:flex;align-items:center;gap:12px}
.brand-mark{width:44px;height:44px;background:var(--green);border-radius:6px}
.brand-name{font-size:46px;font-weight:700;color:var(--green);line-height:1}
.brand-tag{left:120px;top:86px;font-size:17px;color:var(--muted)}
.search{left:600px;top:56px;width:262px;height:32px;border:2px solid var(--green);border-radius:3px;font-size:14px;color:var(--muted);padding:5px 10px}
.search-btn{right:0;top:0;width:32px;height:28px;background:var(--green)}
.socials{left:880px;top:36px;display:flex;gap:10px}
.socials span{width:36px;height:36px;border-radius:50%;background:#d5d5d5;display:block}
.lang{left:900px;top:96px;font-size:15px;color:var(--ink);display:flex;gap:10px;align-items:center}
.lang i{width:22px;height:14px;background:#c9c9c9;display:inline-block}
.nav{left:120px;top:160px;width:960px;height:50px;background:var(--green);display:flex;align-items:center;padding-left:8px}
.nav a{color:var(--white);font-size:13px;font-weight:600;text-decoration:none;padding:0 13px;height:38px;line-height:38px;white-space:nowrap}
.nav a.active{background:var(--white);color:var(--green);border-radius:3px}
/* slider */
.slider{left:120px;top:220px;width:960px;height:440px;background:linear-gradient(120deg,#9aa4b0,#d7dde4 40%,#b67b88 70%,#6f87a6);border-bottom:8px solid var(--green)}
.slide-text{left:90px;top:110px;color:var(--white);font-weight:700;line-height:1.05}
.slide-text .s1{font-size:44px;font-weight:600}
.slide-text .s2{font-size:62px;font-weight:800}
.slide-text .s3{font-size:56px;font-weight:600}
.read-more{left:90px;top:320px;background:#333;color:var(--white);font-size:13px;padding:8px 16px}
.arrow{top:200px;width:36px;height:36px;border-radius:50%;background:rgba(255,255,255,.85)}
/* welcome */
.h-center{left:0;width:1200px;text-align:center;font-size:26px;font-weight:700;color:var(--green)}
.welcome-copy{left:190px;top:768px;width:820px;text-align:center;font-size:14px;line-height:1.6;color:#666}
.go{left:582px;top:888px;width:36px;height:36px}
/* what we do */
.band{left:0;width:1200px;background:var(--band)}
.sec-title{font-size:24px;font-weight:700;color:var(--green)}
.sec-title b{color:#555;font-weight:700}
.rule{height:2px;background:var(--line)}
.tiles{left:120px;top:1064px;display:flex;gap:10px}
.tile{width:184px;height:220px;position:relative}
.tile .label{position:absolute;left:0;bottom:0;width:100%;background:var(--white);font-size:13px;font-weight:600;padding:8px 10px;color:#555}
.tile.first .label{background:var(--green);color:var(--white)}
/* news */
.news{left:120px;top:1448px;display:flex;gap:10px}
.news-item{width:184px}
.news-img{height:86px;position:relative}
.date{position:absolute;left:8px;bottom:-6px;width:38px;height:46px;background:var(--green);color:var(--white);text-align:center;font-size:16px;font-weight:700;line-height:1.1;padding-top:5px}
.date small{display:block;font-size:10px;font-weight:600}
.news-title{margin-top:20px;font-size:12.5px;font-weight:700;color:var(--green);white-space:nowrap}
.news-copy{font-size:12px;color:#777;line-height:1.45;margin-top:4px}
/* clients */
.clients{left:120px;top:1806px;width:960px;display:flex;justify-content:space-between;align-items:center}
.client{font-size:24px;font-weight:700;color:#333;display:flex;align-items:center;gap:8px}
.client i{width:14px;height:14px;background:#333;display:inline-block}
.dots{left:586px;top:1900px;display:flex;gap:6px}
.dots span{width:7px;height:7px;border-radius:50%;background:#bbb}
/* feature */
.video{left:120px;top:1988px;width:480px;height:320px;background:linear-gradient(135deg,#1e1e1e,#3a3a3a 60%,#151515)}
.play{left:200px;top:120px}
.feature{left:620px;width:460px;height:96px;background:#f3f3f3;display:flex}
.feature .icon{width:80px;flex:none;background:var(--green);display:flex;align-items:center;justify-content:center}
.feature .txt{padding:12px 14px;font-size:12px;line-height:1.45;color:#666}
.feature .txt b{display:block;font-size:12.5px;color:#333;margin-bottom:4px}
.feature.on{background:var(--green)}
.feature.on .icon{background:var(--green-dark)}
.feature.on .txt,.feature.on .txt b{color:var(--white)}
/* footer */
.footer{left:0;top:2360px;width:1200px;height:244px;background:var(--green);color:var(--white)}
.foot-h{font-size:15px;font-weight:700;color:var(--white)}
.foot-list{list-style:none;font-size:13px;line-height:2}
.foot-list li::before{content:"";display:inline-block;width:6px;height:6px;background:var(--white);margin-right:8px;vertical-align:middle}
.foot-copy{font-size:13px;line-height:2}
.newsletter{left:780px;top:20px;width:300px;height:190px;background:var(--dark);padding:18px}
.newsletter h4{font-size:20px;font-weight:700;margin-bottom:8px}
.newsletter p{font-size:12px;color:#ccc;line-height:1.45}
.nl-input{margin-top:14px;height:34px;background:var(--white);color:#999;font-size:12px;padding:8px 10px;position:relative}
.nl-btn{position:absolute;right:0;top:0;width:34px;height:34px;background:var(--green)}
</style>
</head>
<body>

<header>
  <div class="abs brand"><span class="brand-mark"></span><span class="brand-name">Velmora</span></div>
  <div class="abs brand-tag">Natural antimicrobial</div>
  <div class="abs search">search...<span class="abs search-btn"></span></div>
  <div class="abs socials"><span></span><span></span><span></span><span></span><span></span></div>
  <div class="abs lang"><i></i>Language: <i></i>English</div>
  <nav class="abs nav">
    <a class="active">HOME</a><a>ABOUT US</a><a>MARKETS</a><a>TECHNOLOGY</a><a>CUSTOMER PROGRAMS</a><a>NEWS HIGHLIGHTS</a><a>CONTACT US</a>
  </nav>
</header>

<section class="abs slider" role="img" aria-label="Photo of colourful garments hanging on a clothing rail">
  <div class="abs slide-text"><div class="s1">CONSUMER</div><div class="s2">HEALTHCARE</div><div class="s3">INDUSTRIAL</div></div>
  <div class="abs read-more">READ MORE</div>
  <span class="abs arrow" style="left:-18px"></span>
  <span class="abs arrow" style="right:-18px"></span>
</section>

<h2 class="abs h-center" style="top:722px">WELCOME TO VELMORA ANTIMICROBIAL</h2>
<p class="abs welcome-copy">Velmora branded antimicrobial technology makes products cleaner and longer lasting with silver, copper and zinc, which have been proven in use throughout history. Velmora antimicrobial technology provides built-in protection by working 24/7 resisting the growth of microbes. We work in close partnership with our customers, from development to end-user marketing, to deliver a product advantage that makes a real difference in the marketplace. Velmora is an EPA registered ionic silver technology and is not a nanosilver technology.</p>
<svg class="abs go" viewBox="0 0 36 36"><circle cx="18" cy="18" r="18" fill="#6cbd45"/><path d="M14 10l9 8-9 8" fill="none" stroke="#fff" stroke-width="3"/></svg>

<section class="abs band" style="top:944px;height:396px">
  <div class="abs sec-title" style="left:120px;top:36px"><b>WHAT</b> WE DO</div>
  <div class="abs rule" style="left:120px;top:80px;width:960px"></div>
</section>
<div class="abs tiles">
  <div class="tile first" role="img" aria-label="Photo of a water filter pitcher" style="background:linear-gradient(#8fb3c7,#dfe9ee)"><span class="label">DRINKING WATER</span></div>
  <div class="tile" role="img" aria-label="Photo of medical instruments" style="background:linear-gradient(#c7cdd3,#8e99a3)"><span class="label">MEDICAL DEVICES</span></div>
  <div class="tile" role="img" aria-label="Photo of folded textiles" style="background:linear-gradient(#5d7fb0,#a9bcd6)"><span class="label">APPAREL &amp; TEXTILES</span></div>
  <div class="tile" role="img" aria-label="Photo of an architectural surface" style="background:linear-gradient(#b9c3cc,#e6eaee)"><span class="label">ARCHITECTURAL SURFACES</span></div>
  <div class="tile" role="img" aria-label="Photo of a laboratory workspace" style="background:linear-gradient(#d9dde0,#aab2b8)"></div>
</div>

<div class="abs sec-title" style="left:120px;top:1376px"><b>NEWS</b> &amp; EVENTS</div>
<div class="abs rule" style="left:120px;top:1420px;width:960px"></div>
<div class="abs news">
  <div class="news-item"><div class="news-img" role="img" aria-label="Photo of a business meeting" style="background:linear-gradient(#a8b4bf,#6d7c89)"><span class="date">07<small>DEC</small></span></div><div class="news-title">Lorem ipsum dolor sit amet</div><div class="news-copy">Consectetur adipiscing elit aliquam erat volutpat nunc porta.</div></div>
  <div class="news-item"><div class="news-img" role="img" aria-label="Photo of a team at work" style="background:linear-gradient(#c9b9a7,#8c7a68)"><span class="date">07<small>DEC</small></span></div><div class="news-title">Lorem ipsum dolor sit amet</div><div class="news-copy">Consectetur adipiscing elit aliquam erat volutpat nunc porta.</div></div>
  <div class="news-item"><div class="news-img" role="img" aria-label="Photo of a presentation" style="background:linear-gradient(#b7c3cc,#7a8a96)"><span class="date">07<small>DEC</small></span></div><div class="news-title">Lorem ipsum dolor sit amet</div><div class="news-copy">Consectetur adipiscing elit aliquam erat volutpat nunc porta.</div></div>
  <div class="news-item"><div class="news-img" role="img" aria-label="Photo of a handshake" style="background:linear-gradient(#d4d8dc,#939ca4)"><span class="date">07<small>DEC</small></span></div><div class="news-title">Lorem ipsum dolor sit amet</div><div class="news-copy">Consectetur adipiscing elit aliquam erat volutpat nunc porta.</div></div>
  <div class="news-item"><div class="news-img" role="img" aria-label="Photo of an office group" style="background:linear-gradient(#b1bcc5,#737f8a)"><span class="date">07<small>DEC</small></span></div><div class="news-title">Lorem ipsum dolor sit amet</div><div class="news-copy">Consectetur adipiscing elit aliquam erat volutpat nunc porta.</div></div>
</div>

<section class="abs band" style="top:1700px;height:250px">
  <div class="abs sec-title" style="left:120px;top:20px"><b>OUR</b> CLIENTS</div>
  <div class="abs rule" style="left:120px;top:64px;width:960px"></div>
</section>
<div class="abs clients">
  <span class="client"><i></i>Corvane</span>
  <span class="client">Halvio</span>
  <span class="client">Ternly</span>
  <span class="client">Fenwick</span>
  <span class="client">Osmera</span>
  <span class="client">Nexapt</span>
  <span class="client">Pravix</span>
</div>
<div class="abs dots"><span></span><span></span><span></span></div>

<section class="abs video" role="img" aria-label="Video still of a person in a workout setting">
  <svg class="abs play" width="80" height="80" viewBox="0 0 80 80"><circle cx="40" cy="40" r="38" fill="#fff"/><path d="M32 24l22 16-22 16z" fill="#2b2b2b"/></svg>
</section>
<div class="abs feature on" style="top:1988px">
  <div class="icon"><svg width="34" height="34" viewBox="0 0 34 34"><rect x="6" y="4" width="22" height="26" fill="none" stroke="#fff" stroke-width="3"/><path d="M11 12h12M11 18h12M11 24h8" stroke="#fff" stroke-width="2"/></svg></div>
  <div class="txt"><b>NEW TO ANTIMICROBIAL SOLUTIONS?</b>Imagine if all the important surfaces in homes, offices and hospitals could resist germs every hour of the day.</div>
</div>
<div class="abs feature" style="top:2100px">
  <div class="icon"><svg width="34" height="34" viewBox="0 0 34 34"><path d="M6 18l8 8 14-16" fill="none" stroke="#fff" stroke-width="4"/></svg></div>
  <div class="txt"><b>WHAT THE VELMORA ADVANTAGE FOR YOUR PRODUCT?</b>Find out how built-in protection adds lasting value and helps your brand stand out.</div>
</div>
<div class="abs feature" style="top:2212px">
  <div class="icon"><svg width="34" height="34" viewBox="0 0 34 34"><circle cx="17" cy="17" r="12" fill="none" stroke="#fff" stroke-width="3"/><path d="M17 10v8l5 3" stroke="#fff" stroke-width="3" fill="none"/></svg></div>
  <div class="txt"><b>OVERVIEW OF CUSTOMER PROGRAMS</b>Welcome to the customer section, where partners find tools, guides and support to launch products.</div>
</div>

<footer class="abs footer">
  <div class="abs foot-h" style="left:120px;top:30px">OTHER LINK</div>
  <ul class="abs foot-list" style="left:120px;top:56px">
    <li>Home</li><li>About Us</li><li>Markets</li><li>Technology</li><li>Customer Programs</li>
  </ul>
  <div class="abs foot-h" style="left:400px;top:30px">CONTACT ADDRESS</div>
  <div class="abs foot-copy" style="left:400px;top:56px">
    240 Ferncliff Road, Lindale, MA 01990<br>555-012-3344<br>info@velmora-labs.com
  </div>
  <div class="abs foot-copy" style="left:400px;top:212px;font-size:11px">&copy; 2014 - 2015 Velmora Labs. All rights reserved.</div>
  <div class="abs newsletter">
    <h4>Get Our Newsletter!</h4>
    <p>Lorem ipsum dolor sit amet, consectetur adipiscing elit. Sign up to receive updates on new solutions.</p>
    <div class="nl-input">Enter your email<span class="nl-btn"></span></div>
  </div>
</footer>

</body>
</html>
```